Child care centre FYLER

looking for a professional yet interesting and fun pastel coloured flyer that is eye catching for Bright Sprouts Early Learning Centre and Kindergarten,

that education children between 6 weeks and 6 years open 6:30 - 6:30 Monday to Friday

Target Market(s)

families with young children

Industry/Entity Type

Education

Requirements
Must have
• *Purpose built architecturally designed centre. *Qualified friendly & Experienced staff. *Educational Programmes. *funded 4 year old kindergarten programs *Fees include all meals, hat and nappies

fully accredited service.
between 6 weeks and 6 years open 6:30 - 6:30 Monday to Friday

```html
<!DOCTYPE html>
<html lang="en">
<head>
<meta charset="utf-8">
<title>Bright Sprouts Early Learning Centre and Kindergarten – Flyer and Postcard</title>
<link rel="stylesheet" href="https://fonts.googleapis.com/css2?family=Short+Stack&family=Open+Sans:wght@400;600&display=swap">
<style>
  :root {
    --page: #efede9;
    --lime: #a9c93b;
    --orange: #f28c1c;
    --teal: #1aa5a5;
    --purple: #7a2e8e;
    --yellow: #f1ea4a;
    --white: #ffffff;
    --line: #9a9a9a;
    --photo-light: #f4ede6;
    --photo-mid: #d9a47e;
    --photo-deep: #b5452f;
  }
  * { box-sizing: border-box; margin: 0; padding: 0; }
  html, body { width: 1018px; height: 1200px; overflow: hidden; }
  body { background: var(--page); position: relative; font-family: "Open Sans", Arial, sans-serif; }

  .flyer {
    position: absolute; left: 123px; top: 62px; width: 662px; height: 510px;
    background: var(--lime); overflow: hidden;
    box-shadow: 0 3px 10px rgba(0,0,0,.18);
  }
  .flyer__photo {
    position: absolute; left: 0; top: 0; width: 345px; height: 100%;
    background: linear-gradient(160deg, var(--photo-light) 0%, var(--photo-light) 35%, var(--photo-mid) 65%, var(--photo-deep) 100%);
  }
  .flyer__header {
    position: absolute; left: 345px; top: 12px; right: 0; height: 133px;
    background: var(--white); border-bottom: 4px solid var(--purple);
  }
  .brand { position: absolute; display: flex; align-items: center; gap: 10px; }
  .brand__dot { width: 30px; height: 30px; border-radius: 50%; background: var(--yellow); flex: none; }
  .brand__name { font-family: "Short Stack", cursive; color: var(--purple); font-size: 34px; line-height: 1; white-space: nowrap; }
  .brand__tag { position: absolute; font-family: "Open Sans", Arial, sans-serif; color: var(--purple); font-size: 12px; white-space: nowrap; }
  .flyer__header .brand { left: 20px; top: 38px; gap: 8px; }
  .flyer__header .brand__dot { width: 22px; height: 22px; }
  .flyer__header .brand__name { font-size: 25px; }
  .flyer__header .brand__tag { left: 50px; top: 76px; font-size: 11px; }

  .features {
    position: absolute; left: 360px; top: 180px; width: 252px; height: 252px;
    border-radius: 50%; background: var(--orange); border: 5px solid var(--white);
    display: flex; flex-direction: column; justify-content: center; align-items: center;
    list-style: none; font-family: "Short Stack", cursive; color: var(--white);
    font-size: 9px; line-height: 1.75; text-align: center; white-space: nowrap;
  }
  .hours {
    position: absolute; left: 274px; top: 348px; width: 132px; height: 132px;
    border-radius: 50%; background: var(--teal); border: 4px solid var(--white);
    display: flex; flex-direction: column; justify-content: center; align-items: center;
    font-family: "Short Stack", cursive; color: var(--white); font-size: 12px; line-height: 1.9;
    white-space: nowrap;
  }
  .splash { position: absolute; border-radius: 50%; background: var(--yellow); }
  .flyer .splash { left: 555px; top: 405px; width: 86px; height: 86px; opacity: .85; }
  .flyer__call {
    position: absolute; left: 468px; top: 444px; font-family: "Short Stack", cursive;
    color: var(--purple); font-size: 12px; white-space: nowrap;
  }
  .flyer__phone {
    position: absolute; left: 476px; top: 464px; display: flex; align-items: center; gap: 6px;
    color: var(--purple); font-size: 18px; font-weight: 600; white-space: nowrap;
  }

  .postcard {
    position: absolute; left: 287px; top: 613px; width: 660px; height: 515px;
    background: var(--white); box-shadow: 0 3px 10px rgba(0,0,0,.18);
  }
  .postcard .brand { left: 44px; top: 70px; }
  .postcard .brand__tag { left: 84px; top: 116px; }
  .postcard .splash { left: 205px; top: 300px; width: 96px; height: 96px; opacity: .75; }
  .postcard__script {
    position: absolute; left: 28px; top: 190px; font-family: "Short Stack", cursive;
    color: var(--purple); font-size: 11px; line-height: 1.9;
  }
  .postcard__script span { display: block; padding-left: 14px; }
  .services { position: absolute; left: 28px; top: 256px; color: var(--purple); font-size: 15px; line-height: 1.5; }
  .services h2 { font-size: 15px; font-weight: 400; }
  .services ul { list-style: none; }
  .services li::before { content: "•"; display: inline-block; width: 26px; padding-left: 2px; }
  .ages { position: absolute; left: 28px; top: 346px; color: var(--purple); font-size: 15px; line-height: 1.45; }
  .contact { position: absolute; left: 28px; top: 444px; color: var(--orange); font-size: 15px; line-height: 1.45; }
  .contact p { display: flex; align-items: center; gap: 5px; }
  .stamp { position: absolute; left: 566px; top: 31px; width: 74px; height: 80px; border: 1.5px solid var(--line); }
  .address-line { position: absolute; left: 380px; width: 222px; border-top: 1px solid var(--line); }
</style>
</head>
<body>

<section class="flyer">
  <div class="flyer__photo" role="img" aria-label="Photograph of a young girl lying on her tummy drawing, surrounded by illustrated alphabet letters and animals"></div>

  <header class="flyer__header">
    <div class="brand"><span class="brand__dot"></span><span class="brand__name">Bright Sprouts</span></div>
    <span class="brand__tag">Early Learning Centre &amp; Kindergarten</span>
  </header>

  <ul class="features">
    <li>Fully Accredited Service</li>
    <li>Purpose built architecturally</li>
    <li>designed centre</li>
    <li>Qualified friendly &amp; Experienced staff</li>
    <li>Educational Programmes</li>
    <li>Funded 4 year old kindergarten programs</li>
    <li>Fees include all meals,</li>
    <li>hat and nappies</li>
  </ul>

  <div class="hours"><span>Monday – Friday</span><span>6:30–6:30</span></div>

  <div class="splash" role="img" aria-label="Yellow paint splash decoration"></div>
  <p class="flyer__call">Call us or come visit!!!</p>
  <p class="flyer__phone">
    <svg width="16" height="20" viewBox="0 0 16 20" aria-hidden="true"><path d="M4 1 L7 5 L5 8 Q7 12 10 14 L12 12 L15 16 L12 19 Q2 15 1 4 Z" fill="var(--purple)"/></svg>
    (03) 5550 1482
  </p>
</section>

<section class="postcard">
  <div class="brand"><span class="brand__dot"></span><span class="brand__name">Bright Sprouts</span></div>
  <span class="brand__tag">Early Learning Centre &amp; Kindergarten</span>

  <p class="postcard__script">Long Day Care<span>an Early Learning Program</span></p>

  <div class="splash" role="img" aria-label="Yellow paint splash decoration"></div>

  <div class="services">
    <h2>SERVICES OFFERED</h2>
    <ul>
      <li>Long Day Care</li>
      <li>an Early Learning Program</li>
    </ul>
  </div>

  <p class="ages">Education children between<br>6 weeks and 6 years</p>

  <div class="contact">
    <p>
      <svg width="12" height="14" viewBox="0 0 16 20" aria-hidden="true"><path d="M4 1 L7 5 L5 8 Q7 12 10 14 L12 12 L15 16 L12 19 Q2 15 1 4 Z" fill="var(--orange)"/></svg>
      (03) 5550 1482
    </p>
    <p>
      <svg width="11" height="15" viewBox="0 0 12 16" aria-hidden="true"><path d="M6 0 A6 6 0 0 1 12 6 C12 10 6 16 6 16 C6 16 0 10 0 6 A6 6 0 0 1 6 0 Z M6 3.5 A2.5 2.5 0 1 0 6 8.5 A2.5 2.5 0 1 0 6 3.5 Z" fill="var(--orange)" fill-rule="evenodd"/></svg>
      18 Wattle Rd Greenvale VIC 3999
    </p>
  </div>

  <div class="stamp"></div>
  <div class="address-line" style="top:246px"></div>
  <div class="address-line" style="top:287px"></div>
  <div class="address-line" style="top:328px"></div>
</section>

</body>
</html>
```